Business Card Kelda Law llc examples and ideas are attached.

in addition to the logo we need a desription what we do: "Reprsenting students with disabilites obtain services to progress in the public school system."

If you can squeeze it on the fron at the bottom great if not put it on the back

```html
<!DOCTYPE html>
<html lang="en">
<head>
<meta charset="utf-8">
<title>Kelda Law llc – Business Card</title>
<link rel="stylesheet" href="https://fonts.googleapis.com/css2?family=Montserrat:wght@400;500;700;800&display=swap">
<style>
  :root {
    --backdrop: #9b9b9b;
    --paper: #f4f5f6;
    --paper-shade: #dfe1e3;
    --navy: #0d2f63;
    --navy-deep: #062654;
    --navy-light: #13488c;
    --steel-blue: #3b8fb8;
    --white: #ffffff;
  }
  * { box-sizing: border-box; margin: 0; padding: 0; }
  html, body {
    width: 1200px; height: 900px; overflow: hidden;
    background: var(--backdrop);
    font-family: "Montserrat", sans-serif;
  }
  .canvas { position: relative; width: 1200px; height: 900px; }

  .card {
    position: absolute;
    width: 560px; height: 320px;
    border-radius: 3px;
    box-shadow: 0 10px 24px rgba(0,0,0,0.25);
    overflow: hidden;
  }

  /* Front */
  .card--front {
    left: 60px; top: 110px;
    background: linear-gradient(160deg, var(--paper) 40%, var(--paper-shade) 100%);
  }
  .card--front .brand {
    position: absolute; left: 60px; top: 136px;
    display: flex; align-items: center; gap: 10px;
    color: var(--steel-blue);
    font-weight: 700; font-size: 22px; letter-spacing: 0.5px;
  }
  .brand__square {
    width: 16px; height: 16px; background: currentColor; flex: none;
  }
  .contact-block { position: absolute; left: 300px; top: 64px; width: 230px; }
  .person-name {
    color: var(--navy);
    font-weight: 800; font-size: 21px; letter-spacing: 0.5px;
    text-transform: uppercase;
  }
  .person-title {
    color: var(--steel-blue);
    font-weight: 400; font-size: 15px; margin-top: 2px;
  }
  .rule { height: 1px; background: var(--steel-blue); margin: 14px 0 14px; }
  .contact-row {
    display: flex; align-items: flex-start; gap: 10px;
    color: var(--navy); font-size: 12.5px; line-height: 1.35;
    margin-bottom: 8px;
  }
  .contact-row svg { flex: none; margin-top: 2px; }

  /* Back */
  .card--back {
    left: 580px; top: 470px;
    background: radial-gradient(ellipse at 40% 45%, var(--navy-light) 0%, var(--navy) 55%, var(--navy-deep) 100%);
    color: var(--white);
  }
  .card--back .brand {
    position: absolute; left: 46px; top: 190px;
    display: flex; align-items: center; gap: 10px;
    color: var(--white);
    font-weight: 700; font-size: 18px; letter-spacing: 0.5px;
  }
  .back-text { position: absolute; left: 200px; top: 88px; width: 330px; }
  .back-text .person-name { color: var(--white); font-size: 24px; }
  .back-title {
    font-weight: 400; font-size: 16px; letter-spacing: 0.5px;
    text-transform: uppercase; margin-top: 2px;
  }
  .mission {
    font-size: 11.5px; line-height: 1.45; margin-top: 10px; opacity: 0.95;
  }
</style>
</head>
<body>
<main class="canvas">

  <section class="card card--front" aria-label="Card front">
    <div class="brand"><span class="brand__square"></span>Kelda Law llc</div>

    <div class="contact-block">
      <h1 class="person-name">Dorian K Vale</h1>
      <p class="person-title">Attorney at Law</p>
      <div class="rule"></div>

      <div class="contact-row">
        <svg width="10" height="13" viewBox="0 0 10 13" aria-hidden="true">
          <path d="M5 0.5a4.3 4.3 0 0 1 4.3 4.3C9.3 8 5 12.5 5 12.5S0.7 8 0.7 4.8A4.3 4.3 0 0 1 5 0.5z" fill="none" stroke="#3b8fb8" stroke-width="1.4"/>
          <circle cx="5" cy="4.8" r="1.5" fill="#3b8fb8"/>
        </svg>
        <span>2741 NE 18<sup style="font-size:8px">th</sup> Ave<br>Bay Harbor FL33150<br>By appointment only</span>
      </div>
      <div class="contact-row">
        <svg width="12" height="12" viewBox="0 0 12 12" aria-hidden="true">
          <path d="M2.5 1h2l1 2.8-1.3 1a6.5 6.5 0 0 0 3 3l1-1.3 2.8 1v2a1 1 0 0 1-1 1A9.5 9.5 0 0 1 1.5 2a1 1 0 0 1 1-1z" fill="#3b8fb8"/>
        </svg>
        <span>555 014 2290</span>
      </div>
      <div class="contact-row">
        <svg width="12" height="10" viewBox="0 0 12 10" aria-hidden="true">
          <rect x="0.5" y="0.5" width="11" height="9" fill="#3b8fb8"/>
          <path d="M0.8 1 6 5.6 11.2 1" fill="none" stroke="#f4f5f6" stroke-width="1.1"/>
        </svg>
        <span>dorian.keldalaw@mail.com</span>
      </div>
    </div>
  </section>

  <section class="card card--back" aria-label="Card back">
    <div class="brand"><span class="brand__square"></span>Kelda Law llc</div>
    <div class="back-text">
      <h2 class="person-name">Dorian K Vale</h2>
      <p class="back-title">Attorney at Law</p>
      <p class="mission">Reprsenting students with disabilites obtain services to progress in the public school system</p>
    </div>
  </section>

</main>
</body>
</html>
```